Brontal Land Associates Web Site

We need a website design for a new land purchasing and development business based in PEI. We are just regular guys trying a new adventure buying small parcels of land, doing the hard work seperating them into lots, building roads and selling off a dream location. We help folks like ourselves buy the lots, create a house plan and help get the project done.

We have a wordpress website, but no skills. The site should have our simple story and links to individual land development progects, currently we have 2. The larger project is on a golf course and images have been uploaded. We would like a map of the properities with locations on the properties you can click to see the views/ pictures. It would be great to have the ability to superimpose house images on the lot images. This would help prospects see the end results. I have attached some photos and logo's, however, they are not manditory.
The project would have to allow for us to update and maintain the site.

Target Market(s)

Visitors to PEI, typically from larger cities in Ontario and Maine. Golfers that want to live on a golf course.

Industry/Entity Type

Realestate (land development)

Coding

Coded - Design and coding required

Number of Pages Required

4 page

Requirements
Must have
• Allow fo us to maintain the site. Company overview page with story and contact information. Links to current realestate projects (developments). Project pages with the informaiton on the land and purchasing. Since this is land not houses, maps to the site, maps of the parcel, maps of the individual lots with the ability to review photos based on the views of that particular lot.
Nice to have
• The ability to upload and overlay a house picture on the lot. This would provide a visual of the final build.

```html
<!DOCTYPE html>
<html lang="en">
<head>
<meta charset="utf-8">
<title>Brontal Land Associates</title>
<link href="https://fonts.googleapis.com/css2?family=Poppins:wght@400;500;600;700;800&display=swap" rel="stylesheet">
<style>
:root{
  --green:#7aad5e;
  --green-dark:#6a9c50;
  --ink:#141414;
  --text:#555;
  --muted:#888;
  --field:#f2f2f2;
  --white:#fff;
  --line:#e6e6e6;
}
*{box-sizing:border-box;margin:0;padding:0}
html,body{width:1200px;height:4313px;overflow:hidden}
body{position:relative;background:var(--white);font-family:'Poppins',sans-serif;color:var(--ink)}
.abs{position:absolute}
a{color:inherit;text-decoration:none}

/* header */
.brand-mark{position:absolute;left:89px;top:17px;width:80px;height:80px;border-radius:50%;background:var(--green)}
.brand-name{position:absolute;left:186px;top:30px;font-weight:600;font-size:22px;line-height:28px;color:var(--ink)}
.brand-sub{position:absolute;left:188px;top:82px;font-weight:600;font-size:7px;letter-spacing:1px;color:var(--ink)}
.nav{position:absolute;top:47px;font-size:13px;font-weight:500;color:var(--ink)}
.nav.active{color:var(--green)}
.nav.active::before{content:"";position:absolute;left:0;right:0;top:-47px;height:2px;background:var(--green)}
.btn-outline{position:absolute;border:2px solid var(--ink);font-weight:600;font-size:12px;display:flex;align-items:center;justify-content:center;color:var(--ink)}

/* hero */
.hero-photo{position:absolute;left:616px;top:112px;width:584px;height:688px;background:linear-gradient(180deg,#cfe1ee 0%,#a9c6de 18%,#7d8f5a 30%,#4f6b34 45%,#6f9a40 70%,#8ab04e 100%)}
.hero-title{position:absolute;left:87px;top:220px;font-size:54px;line-height:67px;font-weight:800;color:var(--ink)}
.hero-title span{color:var(--green)}
.hero-lead{position:absolute;left:89px;top:434px;width:460px;font-size:15px;line-height:25px;color:var(--text)}
.search-bar{position:absolute;left:89px;top:593px;width:1021px;height:108px;background:var(--white);box-shadow:0 12px 40px rgba(0,0,0,.12)}
.field{position:absolute;top:626px;height:42px;background:var(--field);font-size:11px;color:var(--muted);display:flex;align-items:center;padding:0 20px}
.field svg{position:absolute;right:14px;top:17px}
.btn-green{position:absolute;background:var(--green);color:var(--white);font-weight:700;font-size:11px;display:flex;align-items:center;justify-content:center}

/* section headings */
.section-title{position:absolute;left:0;width:1200px;text-align:center;font-weight:800;font-size:36px;color:var(--ink)}
.section-sub{position:absolute;left:0;width:1200px;text-align:center;font-size:13px;color:var(--muted)}

/* steps */
.step{position:absolute;top:984px;width:300px;text-align:center}
.step-icon{width:110px;height:110px;border-radius:50%;background:var(--green);margin:0 auto;display:flex;align-items:center;justify-content:center}
.step h3{margin-top:29px;font-size:18px;font-weight:700}
.step p{margin-top:12px;font-size:14px;line-height:22px;color:var(--text)}

/* story */
.dark-band{position:absolute;left:0;top:1790px;width:1200px;height:361px;background:var(--ink)}
.story-photo{position:absolute;left:0;top:1282px;width:604px;height:581px;background:linear-gradient(180deg,#a4c5df 0%,#cfe0ea 30%,#4c6d34 48%,#6c9449 62%,#557e30 100%)}
.story-title{position:absolute;left:695px;top:1360px;font-size:38px;font-weight:800}
.story-text{position:absolute;left:695px;top:1419px;width:420px;font-size:14.5px;line-height:24px;color:var(--text)}
.insight-title{position:absolute;left:87px;top:1950px;font-size:37px;line-height:49px;font-weight:800;color:var(--white)}
.insight-title span{color:var(--green)}
.insight-art{position:absolute;left:870px;top:1850px;width:330px;height:240px;background:linear-gradient(135deg,rgba(255,255,255,.02),rgba(255,255,255,.07))}

/* locations */
.map-area{position:absolute;left:200px;top:2327px;width:838px;height:569px;background:radial-gradient(ellipse at center,#e9e9e9 0%,#f4f4f4 55%,rgba(255,255,255,0) 75%)}
.map-watermark{position:absolute;left:0;top:2770px;width:1200px;text-align:center;font-size:120px;font-weight:800;letter-spacing:6px;color:#f0f0f0}
.loc-card{position:absolute;width:132px;background:var(--white);box-shadow:0 6px 20px rgba(0,0,0,.1)}
.loc-card .ph{height:95px;background:linear-gradient(180deg,#b9cbd8 0%,#d8c8a8 40%,#6f7f48 62%,#8c8a55 100%)}
.loc-card p{padding:9px 10px 10px;font-size:10px;line-height:15px;font-weight:500;color:var(--ink)}
.pin{position:absolute;width:28px;height:28px;border-radius:50%;background:var(--green);display:flex;align-items:center;justify-content:center;transform:translate(-50%,-50%)}

/* properties */
.prop-card{position:absolute;top:3052px;width:334px;height:505px;background:var(--white);box-shadow:0 8px 30px rgba(0,0,0,.09)}
.prop-card .ph{height:259px;position:relative}
.prop-card .fav{position:absolute;right:18px;top:18px;width:30px;height:30px;border-radius:50%;background:rgba(255,255,255,.45);display:flex;align-items:center;justify-content:center}
.prop-card h3{position:absolute;left:24px;top:283px;width:290px;font-size:20px;line-height:25px;font-weight:700}
.prop-card .fin{position:absolute;left:24px;top:349px;font-size:12px;color:var(--muted)}
.prop-card .price{position:absolute;left:24px;top:383px;font-size:12px;color:var(--muted);display:flex;align-items:center;gap:14px}
.prop-card .price b{font-size:28px;font-weight:700;color:var(--green)}
.prop-card .meta{position:absolute;left:24px;right:24px;top:435px;border-top:1px solid var(--line);padding-top:24px;font-size:11px;color:var(--muted);display:flex;align-items:center}
.prop-card .meta .tour{margin-left:auto;font-weight:700;font-size:14px;color:var(--green)}
.pager{position:absolute;top:3587px;width:43px;height:42px;display:flex;align-items:center;justify-content:center}

/* newsletter + footer */
.newsletter{position:absolute;left:226px;top:3715px;width:747px;height:155px;background:var(--green)}
.newsletter h2{position:absolute;left:0;width:100%;top:28px;text-align:center;font-size:23px;font-weight:700;color:var(--white)}
.newsletter .input{position:absolute;left:89px;top:66px;width:569px;height:44px;background:var(--white);font-size:13px;color:var(--text);display:flex;align-items:center;padding-left:38px}
.foot-logo{position:absolute;left:114px;top:4006px;width:82px;height:82px;border-radius:50%;background:var(--green)}
.foot-name{position:absolute;left:218px;top:4022px;font-size:21px;line-height:26px;font-weight:600;color:var(--white)}
.social{position:absolute;top:4113px;width:37px;height:37px;border-radius:50%;background:#2a2a2a}
.foot-head{position:absolute;top:3986px;font-size:17px;font-weight:700;color:var(--white)}
.foot-links{position:absolute;top:4034px;list-style:none;font-size:13px;line-height:31.5px;color:#ddd}
.foot-links li::before{content:"›";margin-right:8px}
.contact-item{position:absolute;left:877px;display:flex;gap:10px;font-size:12.5px;line-height:18px;color:#ddd}
.copyright{position:absolute;left:0;width:1200px;top:4270px;text-align:center;font-size:13px;font-weight:600;color:#eee}
.chat{position:absolute;left:1133px;top:4230px;width:44px;height:44px;border-radius:50%;background:var(--green);display:flex;align-items:center;justify-content:center}
</style>
</head>
<body>

<!-- header -->
<div class="brand-mark"></div>
<div class="brand-name">Brontal Land<br>Associates</div>
<div class="brand-sub">AT CORRAN VALE GOLF CLUB</div>
<a class="nav active" style="left:544px">HOME</a>
<a class="nav" style="left:614px">PROPERTIES</a>
<a class="nav" style="left:722px">OUR STORY</a>
<a class="nav" style="left:829px">BLOG</a>
<a class="nav" style="left:894px">CONTACT</a>
<a class="btn-outline" style="left:989px;top:37px;width:121px;height:40px">GET NOTIFIED</a>

<!-- hero -->
<div class="hero-photo" role="img" aria-label="Rolling green farmland under a cloudy summer sky"></div>
<h1 class="hero-title"><span>Land</span> Purchasing<br>and Development<br>Business...</h1>
<p class="hero-lead">Visitors to PEI, typically from larger cities in Ontario and Maine. Golfers that want to live on a golf course.</p>
<div class="search-bar"></div>
<div class="field" style="left:124px;width:226px">Where do you want to...<svg width="9" height="6"><path d="M1 1l3.5 3.5L8 1" stroke="#555" stroke-width="1.4" fill="none"/></svg></div>
<div class="field" style="left:360px;width:224px">How did you find us<svg width="9" height="6"><path d="M1 1l3.5 3.5L8 1" stroke="#555" stroke-width="1.4" fill="none"/></svg></div>
<div class="field" style="left:594px;width:148px">Your name</div>
<div class="field" style="left:748px;width:149px">Your email</div>
<a class="btn-green" style="left:917px;top:626px;width:149px;height:42px">SEE PROPERTIES</a>

<!-- how it works -->
<h2 class="section-title" style="top:892px">How it Works</h2>
<p class="section-sub" style="top:942px">How to Purchase a Property</p>
<div class="step" style="left:165px">
  <div class="step-icon"><svg width="50" height="56" viewBox="0 0 50 56" fill="none" stroke="#fff" stroke-width="2.2"><rect x="12" y="3" width="32" height="42" rx="2"/><path d="M20 22l8-7 8 7v9H20z"/><circle cx="14" cy="42" r="8"/><path d="M8 48l-6 6"/></svg></div>
  <h3>Select a Property</h3>
  <p>Aenean sollicitudin lorem quis<br>auctor sem nibh elit duis...</p>
</div>
<div class="step" style="left:448px">
  <div class="step-icon"><svg width="56" height="52" viewBox="0 0 56 52" fill="none" stroke="#fff" stroke-width="2.2"><rect x="10" y="3" width="26" height="32" rx="2"/><path d="M16 12h14M16 19h14M16 26h8"/><path d="M4 38l12-8 10 6 10-6 16 10-12 10H14z"/></svg></div>
  <h3>Sign Agreement</h3>
  <p>Aenean sollicitudin lorem quis<br>auctor sem nibh elit duis...</p>
</div>
<div class="step" style="left:732px">
  <div class="step-icon"><svg width="56" height="52" viewBox="0 0 56 52" fill="none" stroke="#fff" stroke-width="2.2"><circle cx="32" cy="16" r="12"/><path d="M32 9v14M28 13h6a2.5 2.5 0 010 5h-4a2.5 2.5 0 000 5h6"/><path d="M3 36h10l12 4h12a3 3 0 010 6H24M13 48l6 3h16l18-12a3 3 0 00-4-4l-12 7"/></svg></div>
  <h3>Close on Property</h3>
  <p>Aenean sollicitudin lorem quis<br>auctor sem nibh elit duis...</p>
</div>

<!-- story -->
<div class="dark-band"></div>
<div class="story-photo" role="img" aria-label="Tall green grass meadow in front of a tree-lined hillside"></div>
<h2 class="story-title">Our Story</h2>
<p class="story-text">Aenean sollicitudin, lorem quis bibendum auctor, nisi elit consequat ipsum, nec sagittis sem nibh id elit. Duis sed odio sit amet nibh vulputate cursus a sit amet mauris. Morbi accumsan ipsum velit. Nam nec tellus a odio tincidunt auctor a ornare odio. Sed non &nbsp;mauris vitae erat consequat auctor eu in elit. Class aptent taciti sociosqu ad litora torquent per conubia nostra, per inceptos himenaeos. Mauris in erat justo. Nullam ac urna eu felis dapibus condimentum ...</p>
<a class="btn-outline" style="left:696px;top:1664px;width:141px;height:37px;font-size:12px">FIND OUT MORE</a>
<h2 class="insight-title">Get The Insights You Need to Find Your<br>Next Property <span>Investment</span> Opportunity.</h2>
<div class="insight-art" role="img" aria-label="Faint line illustration of hills, trees, sun and cloud"></div>
<a class="btn-green" style="left:944px;top:1997px;width:166px;height:42px">SIGN-UP FOR FREE</a>

<!-- locations -->
<h2 class="section-title" style="top:2232px">Our Locations</h2>
<div class="map-area" role="img" aria-label="Dotted world map showing property locations"></div>
<div class="map-watermark">LOCATIONS</div>
<div class="pin" style="left:353px;top:2394px"><svg width="10" height="13" viewBox="0 0 10 13"><path d="M5 0a5 5 0 00-5 5c0 4 5 8 5 8s5-4 5-8a5 5 0 00-5-5z" fill="#fff"/><circle cx="5" cy="5" r="1.8" fill="#7aad5e"/></svg></div>
<div class="pin" style="left:211px;top:2523px"><svg width="10" height="13" viewBox="0 0 10 13"><path d="M5 0a5 5 0 00-5 5c0 4 5 8 5 8s5-4 5-8a5 5 0 00-5-5z" fill="#fff"/><circle cx="5" cy="5" r="1.8" fill="#7aad5e"/></svg></div>
<div class="pin" style="left:752px;top:2389px"><svg width="10" height="13" viewBox="0 0 10 13"><path d="M5 0a5 5 0 00-5 5c0 4 5 8 5 8s5-4 5-8a5 5 0 00-5-5z" fill="#fff"/><circle cx="5" cy="5" r="1.8" fill="#7aad5e"/></svg></div>
<div class="pin" style="left:501px;top:2620px"><svg width="10" height="13" viewBox="0 0 10 13"><path d="M5 0a5 5 0 00-5 5c0 4 5 8 5 8s5-4 5-8a5 5 0 00-5-5z" fill="#fff"/><circle cx="5" cy="5" r="1.8" fill="#7aad5e"/></svg></div>
<div class="pin" style="left:738px;top:2642px"><svg width="10" height="13" viewBox="0 0 10 13"><path d="M5 0a5 5 0 00-5 5c0 4 5 8 5 8s5-4 5-8a5 5 0 00-5-5z" fill="#fff"/><circle cx="5" cy="5" r="1.8" fill="#7aad5e"/></svg></div>
<div class="pin" style="left:422px;top:2843px"><svg width="10" height="13" viewBox="0 0 10 13"><path d="M5 0a5 5 0 00-5 5c0 4 5 8 5 8s5-4 5-8a5 5 0 00-5-5z" fill="#fff"/><circle cx="5" cy="5" r="1.8" fill="#7aad5e"/></svg></div>
<div class="loc-card" style="left:529px;top:2320px"><div class="ph" role="img" aria-label="Farmland field at dusk"></div><p>65 Acres Farmland<br>in nTractor County,</p></div>
<div class="loc-card" style="left:839px;top:2404px"><div class="ph" role="img" aria-label="Farmland field at dusk"></div><p>65 Acres Farmland<br>in nTractor County,</p></div>
<div class="loc-card" style="left:271px;top:2513px"><div class="ph" role="img" aria-label="Farmland field at dusk"></div><p>65 Acres Farmland<br>in nTractor County,</p></div>
<div class="loc-card" style="left:862px;top:2653px"><div class="ph" role="img" aria-label="Farmland field at dusk"></div><p>65 Acres Farmland<br>in nTractor County,</p></div>
<div class="loc-card" style="left:578px;top:2739px"><div class="ph" role="img" aria-label="Farmland field at dusk"></div><p>65 Acres Farmland<br>in nTractor County,</p></div>

<!-- properties -->
<h2 class="section-title" style="top:2962px">Our Land Properties</h2>
<article class="prop-card" style="left:90px">
  <div class="ph" role="img" aria-label="Green farmland with trees and a mountain behind" style="background:linear-gradient(180deg,#8fb8dc 0%,#c6dceb 30%,#4c6a36 52%,#7ea34a 75%,#9dbb5a 100%)"><span class="fav"><svg width="12" height="12" viewBox="0 0 12 12"><path d="M6 .8l1.6 3.3 3.6.5-2.6 2.5.6 3.6L6 9l-3.2 1.7.6-3.6L.8 4.6l3.6-.5z" fill="#fff"/></svg></span></div>
  <h3>65 Acres of Farmland in Tractor County, MN</h3>
  <p class="fin">Finance Terms: &nbsp;$359/moFor 60 Months</p>
  <p class="price">Price: <b>$220,000</b></p>
  <div class="meta"><span>50 Acreage</span><span style="margin-left:18px">Tractor, MN Location</span><span class="tour">360°</span></div>
</article>
<article class="prop-card" style="left:434px">
  <div class="ph" role="img" aria-label="Golden field at sunset" style="background:radial-gradient(circle at 50% 42%,#ffd58a 0%,#e59a3a 18%,#7a5a3a 45%,#3a3020 60%,#9a7a3a 80%,#c49a4a 100%)"><span class="fav"><svg width="12" height="12" viewBox="0 0 12 12"><path d="M6 .8l1.6 3.3 3.6.5-2.6 2.5.6 3.6L6 9l-3.2 1.7.6-3.6L.8 4.6l3.6-.5z" fill="#fff"/></svg></span></div>
  <h3>50 Acres of Forest in Greenery County, AL</h3>
  <p class="fin">Finance Terms: &nbsp;$359/moFor 60 Months</p>
  <p class="price">Price: <b>$675,000</b></p>
  <div class="meta"><span>50 Acreage</span><span style="margin-left:18px">Tractor, MN Location</span><span class="tour">360°</span></div>
</article>
<article class="prop-card" style="left:778px">
  <div class="ph" role="img" aria-label="Dry open land with a lone shrub under a blue sky" style="background:linear-gradient(180deg,#3a9ac8 0%,#8ec6dc 28%,#b89a78 42%,#c8a888 70%,#b08a68 100%)"><span class="fav"><svg width="12" height="12" viewBox="0 0 12 12"><path d="M6 .8l1.6 3.3 3.6.5-2.6 2.5.6 3.6L6 9l-3.2 1.7.6-3.6L.8 4.6l3.6-.5z" fill="#fff"/></svg></span></div>
  <h3>30 Acres of Forest In Evergreen County, AL</h3>
  <p class="fin">Finance Terms: &nbsp;$359/moFor 60 Months</p>
  <p class="price">Price: <b>$395,000</b></p>
  <div class="meta"><span>50 Acreage</span><span style="margin-left:18px">Tractor, MN Location</span><span class="tour">360°</span></div>
</article>
<a class="pager" style="left:554px;background:var(--green)"><svg width="8" height="12"><path d="M6 1L1.5 6 6 11" stroke="#fff" stroke-width="1.6" fill="none"/></svg></a>
<a class="pager" style="left:603px;background:var(--ink)"><svg width="8" height="12"><path d="M2 1l4.5 5L2 11" stroke="#fff" stroke-width="1.6" fill="none"/></svg></a>

<!-- footer -->
<svg class="abs" style="left:0;top:3700px" width="1200" height="613" viewBox="0 0 1200 613">
  <polygon points="0,65 1200,195 1200,613 0,613" fill="#111"/>
  <polygon points="680,172 1200,190 1200,245" fill="#e4e4e4"/>
</svg>
<section class="newsletter">
  <h2>Subscribe Our Newsletter</h2>
  <div class="input"><svg class="abs" style="left:16px;top:17px" width="13" height="10" viewBox="0 0 13 10"><rect x=".5" y=".5" width="12" height="9" fill="#888"/><path d="M.5.5l6 5 6-5" stroke="#fff" fill="none"/></svg>Enter your email address<svg class="abs" style="right:22px;top:14px" width="18" height="16" viewBox="0 0 18 16"><path d="M1 7l16-6-5 14-3-6z" fill="#7aad5e"/></svg></div>
</section>

<div class="foot-logo"></div>
<div class="foot-name">Brontal Land<br>Associates</div>
<div class="abs" style="left:218px;top:4078px;font-size:7px;font-weight:600;letter-spacing:1px;color:#fff">AT CORRAN VALE GOLF CLUB</div>
<span class="social" style="left:190px" aria-label="Social profile"></span>
<span class="social" style="left:236px" aria-label="Social profile"></span>
<span class="social" style="left:283px" aria-label="Social profile"></span>
<span class="social" style="left:330px" aria-label="Social profile"></span>

<h4 class="foot-head" style="left:509px">Quick Links</h4>
<ul class="foot-links" style="left:509px"><li>Home</li><li>Properties</li><li>Our Story</li><li>Blog</li><li>Contact</li></ul>
<h4 class="foot-head" style="left:680px">Information</h4>
<ul class="foot-links" style="left:680px"><li>Privacy Policy</li><li>Terms &amp; Conditions</li><li>Shipping Policy</li><li>FAQ's</li><li>About Us</li></ul>
<h4 class="foot-head" style="left:877px">Contact info</h4>
<div class="contact-item" style="top:4034px"><svg width="13" height="10" viewBox="0 0 13 10" style="margin-top:4px"><rect width="13" height="10" fill="#7aad5e"/><path d="M0 0l6.5 5L13 0" stroke="#111" fill="none"/></svg><span>Email:<br>info@example.com.au</span></div>
<div class="contact-item" style="top:4087px"><svg width="13" height="13" viewBox="0 0 13 13" style="margin-top:3px"><path d="M3 1l2 3-1.5 1.5a7 7 0 004 4L9 8l3 2-1.5 2.5C6 12 1 7 .5 2.5z" fill="#7aad5e"/></svg><span>Phone:<br>+08 123 456 7890</span></div>
<div class="contact-item" style="top:4141px"><svg width="11" height="14" viewBox="0 0 11 14" style="margin-top:3px"><path d="M5.5 0A5.5 5.5 0 000 5.5C0 10 5.5 14 5.5 14S11 10 11 5.5A5.5 5.5 0 005.5 0z" fill="#7aad5e"/><circle cx="5.5" cy="5.5" r="2" fill="#111"/></svg><span>Location:<br>Some address line goes here<br>city name country</span></div>
<div class="abs" style="left:89px;top:4252px;width:1022px;height:1px;background:#2e2e2e"></div>
<p class="copyright">© Copyright 2022 All rights reserved</p>
<a class="chat" aria-label="Chat"><svg width="22" height="20" viewBox="0 0 22 20"><path d="M11 1C5.5 1 1 4.6 1 9c0 2.3 1.2 4.3 3.2 5.8L3 19l4.6-2.4c1 .3 2.2.4 3.4.4 5.5 0 10-3.6 10-8S16.5 1 11 1z" fill="#fff"/><circle cx="7" cy="9" r="1.2" fill="#7aad5e"/><circle cx="11" cy="9" r="1.2" fill="#7aad5e"/><circle cx="15" cy="9" r="1.2" fill="#7aad5e"/></svg></a>

</body>
</html>
```